Harbor Nightclub

Nightclub flyer., digital single sided, for KV and PX. I included samples of some previous flyers we've used. Sample Info:
HARBOR
FRIDAYS
FRI MAY 1 2020
DJ VORTAN (club floor)
DJ RUZO & DJ TAV (residents on the lounge floor)
4217 Marlow Avenue Sacramento
www.harborvenuehall.example for list/VIP inquiries

Target Market(s)

Upscale top 40 crowd but want some cool and artsy like the examples included.

Font styles to use
Sans Serif

Requirements
Must have
• Harbor Logo
Nice to have
• Would be nice if the flyer can be incorporated later with DJ photos (sometimes we will add dj photos to pixagram etc). Would like a big city type of feel.
Should not have
• Nothing too sexual.

```html
<!DOCTYPE html>
<html lang="en">
<head>
<meta charset="utf-8">
<title>Harbor Nightclub – Friday Flyer</title>
<link rel="stylesheet" href="https://fonts.googleapis.com/css2?family=Archivo:wdth,wght@125,800&family=Oswald:wght@500&family=Poppins:wght@300;400;600&display=swap">
<style>
  :root {
    --stage: #2a2a2e;
    --night: #07050a;
    --deep-violet: #1b1540;
    --club-red: #b3102e;
    --hot-pink: #e8197a;
    --gold: #d9d07a;
    --white: #ffffff;
    --muted: #e6e6ea;
  }
  * { margin: 0; padding: 0; box-sizing: border-box; }
  html, body { width: 1200px; height: 1200px; overflow: hidden; background: var(--stage); }
  .flyer {
    position: absolute; left: 144px; top: 30px;
    width: 912px; height: 1140px; overflow: hidden;
    background: var(--night);
    font-family: "Poppins", sans-serif; color: var(--white);
  }
  .scene-photo {
    position: absolute; inset: 0 0 260px 0;
    background:
      radial-gradient(ellipse at 85% 20%, rgba(214,24,56,.85), transparent 55%),
      radial-gradient(ellipse at 15% 55%, rgba(40,60,170,.7), transparent 50%),
      radial-gradient(ellipse at 70% 60%, rgba(200,20,90,.55), transparent 55%),
      linear-gradient(180deg, var(--deep-violet) 0%, #3a0c2a 60%, var(--night) 100%);
  }
  .scene-fade {
    position: absolute; left: 0; right: 0; top: 560px; height: 340px;
    background: linear-gradient(180deg, transparent, var(--night));
  }
  .accent-shapes { position: absolute; left: 0; top: 0; width: 912px; height: 760px; }
  .dj-photo {
    position: absolute; left: 262px; top: 142px; width: 420px; height: 560px;
    background: radial-gradient(ellipse at 50% 45%, rgba(60,60,70,.85), rgba(30,25,40,.5) 55%, transparent 75%);
  }
  .address {
    position: absolute; top: 66px; left: 0; right: 0; text-align: center;
    font-weight: 400; font-size: 28px; letter-spacing: 5px;
  }
  .event-date {
    position: absolute; left: 556px; top: 402px; width: 292px; height: 62px;
    border: 3px solid var(--white);
    display: flex; align-items: center; justify-content: center; gap: 12px;
    font-family: "Oswald", sans-serif; font-weight: 500; font-size: 33px;
  }
  .event-date .divider { width: 2px; height: 38px; background: var(--white); }
  .lineup { position: absolute; left: 0; right: 0; text-align: center; white-space: nowrap; }
  .headliner {
    font-family: "Archivo", sans-serif; font-weight: 800; font-stretch: 125%;
    font-size: 64px; color: var(--gold); line-height: 1;
  }
  .floor-note { font-weight: 300; font-size: 28px; color: var(--muted); }
  .lineup-club { top: 700px; }
  .lineup-club .floor-note { margin-top: 12px; }
  .lineup-lounge { top: 843px; }
  .lineup-lounge .floor-note { margin-top: 10px; }
  .brand {
    position: absolute; left: 70px; top: 1017px;
    display: flex; align-items: center; gap: 16px;
  }
  .brand-dot { width: 68px; height: 68px; border-radius: 50%; background: var(--white); }
  .brand-name { font-weight: 400; font-size: 36px; letter-spacing: 2px; color: var(--white); }
  .contact { position: absolute; left: 529px; top: 1026px; line-height: 1.3; }
  .contact-url { font-weight: 600; font-size: 20px; }
  .contact-note { font-weight: 300; font-size: 20px; }
</style>
</head>
<body>
  <main class="flyer">
    <div class="scene-photo" role="img" aria-label="Nightclub crowd under red lights with colourful DJ deck light trails"></div>
    <div class="scene-fade"></div>

    <svg class="accent-shapes" viewBox="0 0 912 760" aria-hidden="true">
      <polygon points="174,206 310,206 300,232 190,232" fill="#e8197a"/>
      <polygon points="740,232 780,232 620,470 600,440" fill="#e8197a"/>
      <polygon points="174,206 742,206 449,674" fill="#120c28" opacity="0.92"/>
    </svg>

    <div class="dj-photo" role="img" aria-label="DJ in headphones and cap mixing on decks"></div>

    <p class="address">4217 MARLOW AVENUE SACRAMENTO</p>

    <div class="event-date">
      <span>FRI</span><span class="divider"></span>
      <span>MAY 1</span><span class="divider"></span>
      <span>2020</span>
    </div>

    <section class="lineup lineup-club">
      <h2 class="headliner">DJ VORTAN</h2>
      <p class="floor-note">(club floor)</p>
    </section>

    <section class="lineup lineup-lounge">
      <h2 class="headliner">DJ RUZO &amp; DJ TAV</h2>
      <p class="floor-note">(residents on the lounge floor)</p>
    </section>

    <div class="brand">
      <span class="brand-dot"></span>
      <span class="brand-name">HARBOR</span>
    </div>

    <div class="contact">
      <p class="contact-url">www.harborvenuehall.example</p>
      <p class="contact-note">for list/VIP inquiries</p>
    </div>
  </main>
</body>
</html>
```